Business Card for new Architectural Firm

I intend to practice in a rural mountain community in upstate NY, focusing on residential and light commercial projects, including second home / vacation properties. I wish to convey a feeling of rural outdoorsy modernity.

Color is important - bold and urbane. Secondary or tertiary colors preferred.

Font is important, idiosyncratic is ok

Optionally, I may choose to use the name Brackenfold Studio. If used as part of your design, all of the Must Haves are still required.

Images uploaded are logos I like

Industry/Entity Type

Residential

Contact Information for Business Card

Lionel Harwicke
Architect (This word should stand alone or be associated with my name - not license number)
NY License No. 052816
lionel@designlhq.com
607 382 9154

Font styles to use
Sans Serif
Decorative

Requirements
Must have
• Whatever files I need to best utilize your design
• PDF
• JPG
• EPS
• Vectorwhatsit
Nice to have
• Logo or element that can be incorporated into other print material.
• Could be a font based card
Should not have
• no clip art
• No templates
• no floor plans
• no building photographs

```html
<!DOCTYPE html>
<html lang="en">
<head>
<meta charset="utf-8">
<title>Brackenfold Architecture Studio — Business Card</title>
<link rel="stylesheet" href="https://fonts.googleapis.com/css2?family=Gelasio:wght@400&family=Questrial&display=swap">
<style>
  :root {
    --backdrop: #2f3d45;
    --card: #54473b;
    --leaf-green: #7cc22a;
    --ink-light: #f4f1ea;
  }
  * { box-sizing: border-box; margin: 0; padding: 0; }
  html, body {
    width: 1200px;
    height: 900px;
    overflow: hidden;
    background: var(--backdrop);
  }
  .business-card {
    position: absolute;
    left: 100px;
    top: 164px;
    width: 1000px;
    height: 572px;
    background: var(--card);
    color: var(--ink-light);
  }
  .studio-mark {
    position: absolute;
    left: 40px;
    top: 150px;
    display: flex;
    align-items: center;
    gap: 14px;
    font-family: "Questrial", sans-serif;
    font-size: 29px;
    letter-spacing: 0.5px;
    color: var(--ink-light);
  }
  .studio-mark .mark-dot {
    width: 18px;
    height: 18px;
    border-radius: 50%;
    background: var(--leaf-green);
  }
  .holder {
    position: absolute;
    right: 70px;
    top: 290px;
    display: flex;
    align-items: baseline;
    gap: 16px;
    font-family: "Gelasio", serif;
    font-weight: 400;
    letter-spacing: 0.5px;
  }
  .holder-name {
    font-size: 38px;
    font-weight: 400;
  }
  .holder-title {
    font-size: 24px;
    color: var(--leaf-green);
  }
  .name-rule {
    position: absolute;
    left: 40px;
    right: 68px;
    top: 358px;
    height: 3px;
    background: var(--leaf-green);
  }
  .contact-list {
    position: absolute;
    left: 40px;
    top: 396px;
    list-style: none;
    font-family: "Gelasio", serif;
    font-size: 26px;
  }
  .contact-item {
    display: flex;
    align-items: center;
    gap: 18px;
    height: 51px;
  }
  .contact-icon {
    width: 38px;
    height: 32px;
    flex: none;
  }
</style>
</head>
<body>
  <article class="business-card">
    <div class="studio-mark">
      <span class="mark-dot"></span>
      <span class="studio-name">BRACKENFOLD ARCHITECTURE STUDIO</span>
    </div>

    <div class="holder">
      <h1 class="holder-name">Lionel Harwicke</h1>
      <span class="holder-title">Architect</span>
    </div>
    <div class="name-rule"></div>

    <ul class="contact-list">
      <li class="contact-item">
        <svg class="contact-icon" viewBox="0 0 38 32" aria-hidden="true">
          <path d="M6 22 C4 18 8 10 16 6 C22 3 30 3 33 6 L30 12 C27 10 22 10 18 12 L19 16 C15 18 12 22 12 26 Z" fill="#7cc22a"/>
        </svg>
        <span>607 382 9154</span>
      </li>
      <li class="contact-item">
        <svg class="contact-icon" viewBox="0 0 38 32" aria-hidden="true">
          <rect x="3" y="6" width="32" height="21" fill="none" stroke="#7cc22a" stroke-width="2"/>
          <path d="M3 6 L19 19 L35 6 M3 27 L14 16 M35 27 L24 16" fill="none" stroke="#7cc22a" stroke-width="2"/>
        </svg>
        <span>lionel@designlhq.com</span>
      </li>
      <li class="contact-item">
        <svg class="contact-icon" viewBox="0 0 38 32" aria-hidden="true">
          <path d="M3 16 L9 12 L15 20 L32 4 L36 8 L15 29 Z" fill="#7cc22a"/>
        </svg>
        <span>NY License No. 052816</span>
      </li>
    </ul>
  </article>
</body>
</html>
```